Contractor Plan "B"/Getting Screwed?/Something Useful

We are sending out a series of postcards to a group of local contractors.

The first in the series is: Plan B: Pink Bubble Wrap. Plan A is to buy insurance from my agency. This will be printed, front and back on card stock. We will then glue a piece of bubble wrap to the card and place it in an envelope for delivery.

The second card will be along the same lines but will ask if the client is getting screwed by his current Insurance Company. We will glue a screw in the middle of the card and place the card in an envelope for delivery. On the bottom of we might tell them to call us to get unscrewed.

The third card will follow those lines but say something like: We sent you bubble wrap for your Plan B and you didn't call. Then we sent you something funny but you didn't call. We decided to send you something useful so you might call now! With this card, we are going to send a carpenter pencil.

I am attaching a rough outline of my sketch design for the first card so you will have basic information we will need such as phone number and coverages we offer. If you feel like there is too much info for the size of the card, we can leave some off. I just want the phone to ring! Also, feel free to adjust the wording to make it work better...creative design is not my strong suit!!

I would like for all three cards to be designed. Each can have the same backside. Also, please keep in mind, this is not a postcard so you don't have to leave the blanks on the back for addressing. Each will be mailed in an envelope.

I have also uploaded my logo file as we have recently redone the logo.

Here is more guidance on the project: The cards are going to be 10 cm wide and 23 cm tall. I have added more wording in the brief. Also, I attached a word doc with a good idea of what to use for wording. Basically I want the following idea: Card 1: At top of card - Plan B: Pink Bubble Wrap Below the bubble wrap - Plan A: Call us so you don't have to use Pink Bubble Wrap Card 2: At top of card - Getting Screwed? Is your current agent taking you for granted? Below the area where we are going to glue a screw - Get unscrewed, Call us! Card 3: At top of card - We have the sharpest pencil in town! We will leave space for a carpenter pencil to be attached tot he card. On the other side of the open space - Call us today for the best rates on your insurance!

Please review the attached word doc for an idea of what to put on the back of the card. To be clear, we need three designs for the front of the card and can probably use just one design for the back of all three. If you think we need to have a different design for the back of each, I would like to see your ideas. Thank you for your hard work on these!

Reason: Hi, I am extending the time as I am expecting a few more submissions. Thank you!

Target Market(s)

We are targeting both contractors and truckers with this campaign.

Industry/Entity Type

Insurance

Requirements
Must have
• Clever wording. It needs to be a call to action and doesn't need to have too many specifics.

We also have to have space in the middle to glue the bubble wrap on the first card, the screw in the second and attach the pencil in the third.

```html
<!DOCTYPE html>
<html lang="en">
<head>
<meta charset="utf-8">
<title>Contractor Card Series</title>
<link rel="stylesheet" href="https://fonts.googleapis.com/css2?family=Montserrat:ital,wght@0,400;0,500;0,600;0,700;0,800;1,500&display=swap">
<style>
  :root {
    --ink: #000000;
    --paper: #ffffff;
    --pink: #d18bbd;
    --slate: #7f9ca5;
    --orange: #f7b234;
    --red: #e30613;
  }
  * { margin: 0; padding: 0; box-sizing: border-box; }
  html, body { width: 1200px; height: 576px; overflow: hidden; background: var(--paper); }
  body { position: relative; font-family: "Montserrat", Arial, sans-serif; color: var(--ink); }

  .card {
    position: absolute; top: 12px; width: 239px; height: 554px;
    border: 2px solid var(--ink); background: var(--paper); text-align: center;
  }
  .card--plan-b { left: 11px; }
  .card--screwed { left: 322px; }
  .card--useful { left: 635px; }
  .card--back { left: 947px; }

  .card > * { position: absolute; left: 0; right: 0; }

  .headline { font-weight: 700; font-size: 35px; line-height: 36px; letter-spacing: 0.5px; }
  .intro { font-weight: 500; font-size: 16.5px; line-height: 22px; }

  .band {
    top: 119px; height: 48px; color: var(--paper); font-weight: 700;
    display: flex; align-items: center; justify-content: center; flex-direction: column;
  }
  .band--pink { background: var(--pink); font-size: 22px; }
  .band--slate { background: var(--slate); font-size: 12.5px; font-weight: 600; line-height: 18px; }
  .band--orange { background: var(--orange); font-size: 20px; line-height: 21px; font-weight: 600; }
  .band--red { background: var(--red); font-size: 14.5px; font-weight: 600; line-height: 19px; }

  .cta { top: 356px; font-weight: 700; font-size: 16.5px; line-height: 28px; }
  .cta__accent { font-size: 22px; font-weight: 700; letter-spacing: 0.5px; }
  .cta__accent--pink { color: var(--pink); }
  .cta__accent--slate { color: var(--slate); }

  .phone {
    top: 414px; height: 48px; color: var(--paper); font-weight: 700; font-size: 31px;
    display: flex; align-items: center; justify-content: center; letter-spacing: 0.3px;
  }
  .phone--pink { background: var(--pink); }
  .phone--slate { background: var(--slate); }
  .phone--orange { background: var(--orange); }
  .phone--red { background: var(--red); }

  .footnote { top: 472px; font-size: 12px; line-height: 16px; font-weight: 500; }

  .brand {
    top: 28px; display: flex; align-items: center; justify-content: center; gap: 8px;
    font-weight: 800; font-size: 19px; line-height: 24px; color: var(--ink);
  }
  .brand__mark { width: 18px; height: 18px; background: var(--red); flex: none; }
  .brand__name { text-align: left; }
  .brand__tag { top: 92px; font-size: 16px; font-weight: 600; letter-spacing: 0.3px; }

  .coverage { top: 182px; list-style: none; font-size: 12px; font-weight: 700; line-height: 16.4px; }
  .promise { top: 294px; font-size: 12px; font-weight: 500; line-height: 16.4px; }
  .rates { top: 343px; font-size: 12px; font-weight: 500; line-height: 16.4px; }
  .rates__web { font-weight: 700; }
  .address { top: 489px; font-size: 11px; font-weight: 500; }
</style>
</head>
<body>

<section class="card card--plan-b">
  <h2 class="headline" style="top:38px;color:var(--pink);">PLAN B</h2>
  <p class="intro" style="top:74px;">Protect your business<br>with</p>
  <div class="band band--pink">Pink Bubble Wrap</div>
  <p class="cta">Call us so you don’t have<br>to use <span class="cta__accent cta__accent--pink">PLAN B</span></p>
  <div class="phone phone--pink">555-014-2738</div>
  <p class="footnote">Why pink?<br>You might not get sued<br>if they think you are a <em>wuss</em>.</p>
</section>

<section class="card card--screwed">
  <h2 class="headline" style="top:24px;color:var(--slate);">GETTING<br>SCREWED?</h2>
  <div class="band band--slate">Is your current insurance<br>company taking you for granted?</div>
  <p class="cta">Get unscrewed,<br><span class="cta__accent cta__accent--slate">CALL US!</span></p>
  <div class="phone phone--slate">555-014-2738</div>
</section>

<section class="card card--useful">
  <p class="intro" style="top:18px;font-size:15.5px;line-height:20.5px;">We sent some bubble wrap,<br>you didn’t call.<br>We offered to unscrew you<br>and we didn’t hear back.</p>
  <div class="band band--orange">Perhaps<br>something useful?</div>
  <p class="cta">We hope you’ll call us<br><span class="cta__accent cta__accent--slate">NOW!</span></p>
  <div class="phone phone--orange">555-014-2738</div>
</section>

<section class="card card--back">
  <div class="brand"><span class="brand__mark"></span><span class="brand__name">HARBOR POINT<br>INSURANCE</span></div>
  <div class="band band--red">YOUR SOURCE<br>FOR ALL THINGS INSURANCE</div>
  <ul class="coverage">
    <li>Builders Risk</li>
    <li>Property</li>
    <li>Workers Compensation</li>
    <li>General Liability</li>
    <li>Flood</li>
    <li>Health</li>
  </ul>
  <p class="promise">Our job is to make sure<br>you can sleep at night.</p>
  <p class="rates">Call us today to get the best rates<br>from multiple insurance carriers.<br><span class="rates__web">www.harborpointinsure.com</span></p>
  <div class="phone phone--red">555-014-2738</div>
  <p class="address">4810 Maple Ridge Rd, Brookfield, Texas 77000</p>
</section>

</body>
</html>
```